Exterior cleaning company requires a eye catching a5 leaflet

we need some updated leaflet designs, a5 folded, we are targeting all exterior cleaning contracts, including roof cleaning & treatment, render cleaning & Treatment, driveways, block paving cleaning using the latest in low pressure cleaning technologies along side high pressure jetwashing. gutter clearance and flushing, water fed telescopic pole window cleaning of difficult to reach windows and high buildings. our website : www.tkbellowsec.co.uk facebook page: https://www.facebook.com/tkbellowsexteriorcareltd Instagram: https://www.instagram.com/tkbellowsec/ a quick google search of roof cleaning, soft washing etc will provide results of what we are doing

Target Market(s)

home owners, commercial clients

Font styles to use
Serif
Sans Serif

Requirements
Must have
• A5 Landscape folded leaflet, front page with company information and bullet points of main works : window & conservatory cleaning, roof cleaning & treatment, Render cleaning & treatment, pressure washing, soft washing, gutter clearing, pressure washing of patios, driveways, gutters, fascias (more info can be provided on techniques etc if required)

```html
<!DOCTYPE html>
<html lang="en">
<head>
<meta charset="utf-8">
<title>TK Bellows Exterior Care – A5 Leaflet</title>
<link href="https://fonts.googleapis.com/css2?family=Montserrat:wght@300;400;500;600;700&family=Lato:wght@400;700&display=swap" rel="stylesheet">
<style>
  :root{
    --navy:#1d3f7a;
    --navy-deep:#12295a;
    --blue:#2a5aa8;
    --sky:#9fb6d8;
    --pale:#eef2f8;
    --ink:#2b2b2b;
    --grey:#555;
    --stage:#e4e4e4;
    --white:#ffffff;
  }
  *{box-sizing:border-box;margin:0;padding:0}
  html,body{width:1200px;height:1200px;overflow:hidden}
  body{background:var(--stage);position:relative;font-family:"Lato",sans-serif;color:var(--ink)}
  .page{position:absolute;width:580px;height:410px;background:var(--white);overflow:hidden;box-shadow:0 2px 8px rgba(0,0,0,.12)}
  .front{left:20px;top:150px}
  .back{left:600px;top:150px}
  .spread{position:absolute;left:20px;top:620px;width:1160px;height:410px;box-shadow:0 2px 8px rgba(0,0,0,.12)}

  /* front cover */
  .front .side-panel{position:absolute;left:0;top:0;width:210px;height:410px;
    background:linear-gradient(160deg,#2d5596 0%,var(--navy) 55%,var(--navy-deep) 100%);color:var(--white);padding:34px 22px 0 26px}
  .eyebrow{font-family:"Montserrat",sans-serif;font-weight:600;font-size:10px;letter-spacing:.06em;text-transform:uppercase;line-height:1.25}
  .cover-title{font-family:"Montserrat",sans-serif;font-weight:500;font-size:29px;line-height:1.02;letter-spacing:.04em;text-transform:uppercase;margin-top:4px}
  .work-list{list-style:none;margin-top:26px}
  .work-list li{font-family:"Montserrat",sans-serif;font-size:9.5px;line-height:1.2;margin-bottom:5px;padding-left:16px;position:relative}
  .work-list li::before{content:"";position:absolute;left:2px;top:2px;width:6px;height:8px;background:var(--sky);border-radius:50% 50% 50% 50%/60% 60% 40% 40%}
  .site-link{position:absolute;left:26px;bottom:26px;font-family:"Montserrat",sans-serif;font-size:9.5px}
  .site-link::before{content:"";display:block;width:22px;height:1px;background:var(--white);margin-bottom:6px}
  .front .window-field{position:absolute;left:210px;top:0;width:370px;height:410px;background:linear-gradient(180deg,#f7f8fa,#eceff3)}
  .hero-photo{position:absolute;left:300px;top:30px;width:170px;height:170px;border-radius:50%;background:linear-gradient(160deg,#c9d6ea,#7f98c0 60%,#4d6a9a)}
  .brand{position:absolute;display:flex;align-items:center;gap:8px}
  .brand .dot{width:34px;height:34px;border-radius:50%;border:1.5px solid var(--grey)}
  .brand .name{font-family:"Montserrat",sans-serif;font-weight:600;font-size:15px;line-height:1.05;color:var(--ink)}
  .brand .name small{display:block;font-size:8px}
  .front .brand{left:260px;top:300px}
  .call{position:absolute;left:415px;top:302px;border-left:1.5px solid var(--navy);padding-left:7px;font-family:"Montserrat",sans-serif;color:var(--navy)}
  .call .label{font-size:9px;font-weight:600;color:var(--blue)}
  .call .num{font-size:14px;font-weight:400}

  /* back cover */
  .photo-grid{position:absolute;left:0;top:0;width:580px;height:190px;display:grid;grid-template-columns:repeat(5,1fr);grid-template-rows:repeat(2,1fr)}
  .photo-grid .blank{background:var(--white)}
  .photo-grid .shot{background:linear-gradient(160deg,#d0d0d0,#7a7a7a)}
  .photo-grid .shot.warm{background:linear-gradient(160deg,#8fb6e0,#c4a676 70%,#8c7a64)}
  .back .water{position:absolute;left:0;top:190px;width:580px;height:220px;background:linear-gradient(180deg,#1f4fa3,var(--navy-deep))}
  .back .halo{position:absolute;left:150px;top:170px;width:300px;height:300px;border-radius:50%;background:rgba(255,255,255,.12)}
  .back .brand{left:205px;top:230px}
  .back .brand .dot{border-color:var(--white)}
  .back .brand .name{color:var(--white)}
  .contact-list{position:absolute;left:205px;top:280px;list-style:none;color:var(--white);font-family:"Montserrat",sans-serif;font-size:9.5px}
  .contact-list li{display:flex;align-items:center;gap:6px;margin-bottom:3px}
  .contact-list svg{width:10px;height:10px;flex:none}

  /* inner spread */
  .spread .half{position:absolute;top:0;width:580px;height:410px;background:var(--white);overflow:hidden}
  .spread .half.left{left:0}
  .spread .half.right{left:580px;box-shadow:inset 14px 0 14px -12px rgba(0,0,0,.18)}
  .spread-title{position:absolute;top:16px;font-family:"Montserrat",sans-serif;font-weight:300;font-size:40px;line-height:1;letter-spacing:.04em;color:var(--navy);white-space:nowrap;writing-mode:vertical-rl}
  .left .spread-title{left:4px;transform:rotate(180deg)}
  .right .spread-title{right:4px}
  .frame{position:absolute;top:8px;width:92px;height:262px;border:1px solid var(--navy)}
  .left .frame{left:48px;border-left:none}
  .right .frame{right:48px;border-right:none}
  .thumbs{position:absolute;top:20px;width:66px;display:flex;flex-direction:column;gap:6px}
  .left .thumbs{left:58px}
  .right .thumbs{right:58px}
  .thumbs div{height:54px;background:linear-gradient(160deg,#a9bcd6,#6b7f99)}
  .thumbs div:nth-child(2){background:linear-gradient(160deg,#7fc4e6,#3b7fae)}
  .thumbs div:nth-child(3){background:linear-gradient(160deg,#c3a98a,#6e5a47)}
  .service{position:absolute;width:380px}
  .left .service{left:152px;text-align:right;padding-right:34px}
  .right .service{left:48px;padding-left:34px}
  .service h3{font-family:"Montserrat",sans-serif;font-weight:500;font-size:10px;letter-spacing:.06em;text-transform:uppercase;color:var(--ink);margin-bottom:3px}
  .service p{font-size:6.6px;line-height:1.3;color:var(--grey)}
  .service svg{position:absolute;top:6px;width:20px;height:20px}
  .left .service svg{right:4px}
  .right .service svg{left:4px}
  .wave{position:absolute;left:0;top:286px;width:580px;height:124px}
  .about{position:absolute;top:354px;left:30px;width:530px;color:var(--white);font-size:6.4px;line-height:1.35}
  .about p{margin-bottom:3px}
</style>
</head>
<body>

<section class="page front" aria-label="Front cover">
  <div class="window-field"></div>
  <div class="side-panel">
    <p class="eyebrow">Most reliable<br>professional</p>
    <h1 class="cover-title">Cleaning<br>Services</h1>
    <ul class="work-list">
      <li>Window &amp;<br>conservatory cleaning</li>
      <li>Roof cleaning &amp; treatment</li>
      <li>Render cleaning &amp; treatment</li>
      <li>Pressure washing</li>
      <li>Soft washing</li>
      <li>Gutter clearing</li>
      <li>Pressure washing of patios</li>
      <li>Driveways</li>
      <li>Gutters</li>
      <li>Fascias</li>
    </ul>
    <p class="site-link">www.tkbellowsec.co.uk</p>
  </div>
  <div class="hero-photo" role="img" aria-label="Operative abseiling down a glass office facade cleaning the windows"></div>
  <div class="brand"><span class="dot"></span><span class="name">TK Bellows<small>Exterior Care Ltd</small></span></div>
  <div class="call"><div class="label">Call Us</div><div class="num">01632 960 418</div></div>
</section>

<section class="page back" aria-label="Back cover">
  <div class="photo-grid">
    <div class="blank"></div>
    <div class="shot warm" role="img" aria-label="Cleaning a retail store frontage from a lift"></div>
    <div class="blank"></div>
    <div class="shot" role="img" aria-label="Clean tiled roof and white fascia"></div>
    <div class="shot" role="img" aria-label="Company vans parked by a glazed building"></div>
    <div class="shot" role="img" aria-label="Operative washing a large roof with a pole"></div>
    <div class="blank"></div>
    <div class="shot" role="img" aria-label="Modern glass office building"></div>
    <div class="blank"></div>
    <div class="blank"></div>
  </div>
  <div class="water" role="img" aria-label="Deep blue water splash"></div>
  <div class="halo"></div>
  <div class="brand"><span class="dot"></span><span class="name">TK Bellows<small>Exterior Care Ltd</small></span></div>
  <ul class="contact-list">
    <li><svg viewBox="0 0 10 10"><path d="M2 1l2 2-1 1.2c.6 1.2 1.5 2.1 2.8 2.8L7 6l2 2-1.2 1.2C4.5 9 1 5.5.8 2.2z" fill="#fff"/></svg>01632 960 418</li>
    <li><svg viewBox="0 0 10 10"><rect x=".8" y="2" width="8.4" height="6" fill="none" stroke="#fff"/><path d="M.8 2L5 5.5 9.2 2" fill="none" stroke="#fff"/></svg>info@tkbellowsec.co.uk</li>
    <li><svg viewBox="0 0 10 10"><path d="M5 .5a3 3 0 013 3c0 2.3-3 6-3 6s-3-3.7-3-6a3 3 0 013-3z" fill="#fff"/><circle cx="5" cy="3.5" r="1" fill="#1d3f7a"/></svg>14 alder lane, formby, l37 2xq</li>
    <li><svg viewBox="0 0 10 10"><circle cx="5" cy="5" r="4" fill="none" stroke="#fff"/><path d="M1 5h8M5 1c-2 2.5-2 5.5 0 8M5 1c2 2.5 2 5.5 0 8" fill="none" stroke="#fff" stroke-width=".7"/></svg>www.tkbellowsec.co.uk</li>
    <li><svg viewBox="0 0 10 10"><circle cx="5" cy="5" r="4" fill="#fff"/></svg>www.facebook.com/tkbellowsexteriorcareltd</li>
    <li><svg viewBox="0 0 10 10"><circle cx="5" cy="5" r="4" fill="#fff"/></svg>www.instagram.com/tkbellowsec/</li>
  </ul>
</section>

<section class="spread" aria-label="Inside spread: services">
  <svg width="0" height="0" style="position:absolute">
    <defs>
      <symbol id="drop-badge" viewBox="0 0 20 20">
        <circle cx="10" cy="10" r="9" fill="none" stroke="#c5d2e6" stroke-width="1.2"/>
        <path d="M10 4.5c2.3 3 3.3 4.8 3.3 6.4a3.3 3.3 0 01-6.6 0c0-1.6 1-3.4 3.3-6.4z" fill="#9fb6d8"/>
      </symbol>
      <linearGradient id="sea" x1="0" y1="0" x2="0" y2="1">
        <stop offset="0" stop-color="#2a5aa8"/>
        <stop offset="1" stop-color="#12295a"/>
      </linearGradient>
    </defs>
  </svg>

  <div class="half left">
    <div class="frame"></div>
    <div class="thumbs">
      <div role="img" aria-label="Terrace of town houses"></div>
      <div role="img" aria-label="Window cleaning with water fed pole over glass"></div>
      <div role="img" aria-label="Brick house with conservatory"></div>
      <div role="img" aria-label="Rooftop solar panels"></div>
    </div>
    <h2 class="spread-title">SERVICES</h2>

    <article class="service" style="top:24px">
      <h3>External Windows</h3>
      <p>Our staff use the reach &amp; wash system otherwise known as the 'water fed pole'. A technique which, compared to traditional window cleaning, enables us to reach your windows and frames safely from the ground.</p>
      <svg><use href="#drop-badge"/></svg>
    </article>
    <article class="service" style="top:82px">
      <h3>Internal Windows</h3>
      <p>We clean internal windows and mirrors using the dragonfly system. This method, also using purified water, can reach those hard to access windows again safely from the ground.</p>
      <svg><use href="#drop-badge"/></svg>
    </article>
    <article class="service" style="top:143px">
      <h3>Conservatory Roofs</h3>
      <p>Has your conservatory roof started to turn green, full of bird muck or dirt? Our water pole method 99% of the time gets rid of all the dirt and grime building up that's left on your roof.</p>
      <svg><use href="#drop-badge"/></svg>
    </article>
    <article class="service" style="top:198px">
      <h3>Solar Panels</h3>
      <p>Using our access equipment we can clean your solar panels. Anything that blocks the light transmission to your solar PV or thermal panels has the potential to lower the performance.</p>
      <svg><use href="#drop-badge"/></svg>
    </article>

    <svg class="wave" viewBox="0 0 580 124" preserveAspectRatio="none" role="img" aria-label="Blue water wave band">
      <path d="M0 40 C60 20 110 50 170 32 S280 18 340 36 S470 52 580 30 V124 H0Z" fill="url(#sea)"/>
      <path d="M0 36 C60 16 110 46 170 28 S280 14 340 32 S470 48 580 26" fill="none" stroke="#9fb6d8" stroke-width="1" opacity=".6"/>
    </svg>
    <div class="about">
      <p>TK Bellows Exterior Care is Formby's most reliable, professional cleaning company, who have been providing cleaning services across the North West for 20 years!</p>
      <p>At TK Bellows, our mission is to lead our sector in providing all of our customers with an outstanding cleaning service that keeps us ahead of our competitors. All of our staff are uniformed, polite, courteous and always happy to help. We aim to build long lasting relationships with our customers, and offer a 1st class customer service team to help resolve any issues that may arise.</p>
    </div>
  </div>

  <div class="half right">
    <div class="frame"></div>
    <div class="thumbs">
      <div role="img" aria-label="Clean white fascias and gutters"></div>
      <div role="img" aria-label="Freshly cleaned block paving driveway"></div>
      <div role="img" aria-label="Gutter vacuum clearing in progress"></div>
      <div role="img" aria-label="Pressure washed building exterior"></div>
    </div>
    <h2 class="spread-title">SERVICES</h2>

    <article class="service" style="top:18px">
      <h3>Fascias &amp; Gutters</h3>
      <p>Using our telescopic pressure washing lance, we can clean all of your UPVC fascias, gutters and drain pipes safely from the ground. The end result: your fascias and gutters looking like brand new again.</p>
      <svg><use href="#drop-badge"/></svg>
    </article>
    <article class="service" style="top:82px">
      <h3>Driveways &amp; Patios</h3>
      <p>From small patio areas to large driveways we clean it all. TK Bellows specialise in all driveway and patio cleaning, from Indian stone, tarmac and concrete flags to block paving.</p>
      <svg><use href="#drop-badge"/></svg>
    </article>
    <article class="service" style="top:138px">
      <h3>Gutter Cleaning</h3>
      <p>Your property's gutters and downpipes accumulate all sorts of debris brought by the wind. Using our high reach vac we can clean the gutters safely from the ground, eliminating any falls from height.</p>
      <svg><use href="#drop-badge"/></svg>
    </article>
    <article class="service" style="top:198px">
      <h3>Pressure Washing</h3>
      <p>We offer a wide range of pressure washing services, from garden furniture to house roofs, at competitive prices. Cleaning and restoration of all hard surfaces in both the domestic and commercial market.</p>
      <svg><use href="#drop-badge"/></svg>
    </article>

    <svg class="wave" viewBox="0 0 580 124" preserveAspectRatio="none" role="img" aria-label="Blue water wave band">
      <path d="M0 30 C90 50 170 22 250 38 S400 52 460 32 S540 22 580 38 V124 H0Z" fill="url(#sea)"/>
      <path d="M0 26 C90 46 170 18 250 34 S400 48 460 28 S540 18 580 34" fill="none" stroke="#9fb6d8" stroke-width="1" opacity=".6"/>
    </svg>
    <div class="about">
      <p>Whether it's to improve overall results or safety, we are always on the lookout for the latest equipment that gives the best finish possible. At TK Bellows we use the reach &amp; wash system, otherwise known as the 'water fed pole'.</p>
      <p>Our window cleaning round varies from domestic houses to commercial buildings, shops, schools, factories, blocks of flats and more. Please refer to the 'services' page of our website for further information on other aspects of our cleaning.</p>
    </div>
  </div>
</section>

</body>
</html>
```